New Zealand Export company needs business cards

We need new business cards to match our new logo for a company based in New Zealand who deal specifically with the Pacific Islands. We source, consolidate and ship products out of New Zealand to the Pacific Islands. Will attach our old ones and also new logo.
Would like the Islands we deal with and the areas of work we have access to, to be included on the business cards.

Contact Information for Business Card

T +64 9 571 3048
F +64 9 571 6285
12-18 Kowhai Lane, Harlow Bay, 0999
PO Box 814, Harlow Bay, Auckland 0998, New Zealand
www.falconfreight.example.nz
E sales@falconfreight.example.nz

Font styles to use
Sans Serif

Colors
85abd2
33a6d7
ffffff

Requirements
Must have
• A company of PWM

```html
<!DOCTYPE html>
<html lang="en">
<head>
<meta charset="utf-8">
<title>Falcon Freight – Business Cards</title>
<link href="https://fonts.googleapis.com/css2?family=Poppins:wght@400;500;600&display=swap" rel="stylesheet">
<style>
  :root {
    --backdrop: #77787a;
    --card: #1e1f21;
    --blue-deep: #0c52a6;
    --blue-light: #34a8e0;
    --text-muted: #9b9c9f;
    --divider: #4a4b4e;
  }
  * { margin: 0; padding: 0; box-sizing: border-box; }
  html, body {
    width: 1200px; height: 960px; overflow: hidden;
    background: var(--backdrop);
    font-family: "Poppins", sans-serif;
  }
  .sheet {
    position: relative; width: 1200px; height: 960px;
    display: flex; flex-direction: column; align-items: center;
    justify-content: center; gap: 48px;
  }
  .card {
    position: relative; width: 720px; height: 411px;
    background: var(--card);
    box-shadow: 0 10px 24px rgba(0,0,0,.35);
    overflow: hidden;
  }
  /* Front */
  .card--front { display: flex; align-items: center; justify-content: center; }
  .wordmark {
    color: var(--blue-deep); font-weight: 600; text-transform: uppercase;
    text-align: center; line-height: 1;
  }
  .wordmark__top { font-size: 72px; letter-spacing: 2px; display: block; }
  .wordmark__bottom { font-size: 34px; letter-spacing: 18px; display: block; margin-top: 10px; padding-left: 18px; }

  /* Back */
  .brand {
    position: absolute; left: 48px; top: 46px;
    display: flex; align-items: center; gap: 14px;
  }
  .brand__square { width: 40px; height: 40px; background: var(--blue-deep); }
  .brand__name {
    color: var(--blue-deep); font-weight: 600; font-size: 30px;
    letter-spacing: 1px; text-transform: uppercase; line-height: 1;
  }
  .bands { position: absolute; left: 0; top: 0; }
  .band-label {
    position: absolute; height: 46px; display: flex; align-items: center;
    font-weight: 500; text-transform: uppercase;
    font-size: 20px; letter-spacing: .5px; line-height: 1; white-space: nowrap;
  }
  .band-label--person { left: 60px; top: 236px; color: var(--blue-deep); }
  .band-label--role { left: 350px; top: 190px; color: var(--blue-light); }
  .details {
    position: absolute; left: 48px; right: 48px; bottom: 36px;
    display: flex; align-items: stretch; gap: 28px;
    color: var(--text-muted); font-size: 15px; line-height: 1.5;
  }
  .details__address { font-style: normal; }
  .details__divider { width: 1px; background: var(--divider); }
</style>
</head>
<body>
<main class="sheet">
  <section class="card card--front" aria-label="Card front">
    <div class="wordmark">
      <span class="wordmark__top">Falcon</span>
      <span class="wordmark__bottom">Freight</span>
    </div>
  </section>

  <section class="card card--back" aria-label="Card back">
    <svg class="bands" width="720" height="411" viewBox="0 0 720 411" aria-hidden="true">
      <polygon points="0,236 300,236 340,282 0,282" fill="var(--blue-light)"/>
      <polygon points="300,190 720,190 720,236 300,236 340,282" fill="var(--blue-deep)"/>
      <polygon points="270,236 300,190 300,236" fill="var(--blue-deep)"/>
      <polygon points="540,144 720,144 720,190 600,190" fill="var(--blue-light)"/>
    </svg>
    <div class="brand">
      <span class="brand__square"></span>
      <span class="brand__name">Falcon Freight</span>
    </div>
    <p class="band-label band-label--person">Tessa Halloran</p>
    <p class="band-label band-label--role">Sales Manager</p>
    <div class="details">
      <address class="details__address">
        12-18 Kowhai Lane, Harlow Bay, 0999<br>
        PO Box 814, Harlow Bay<br>
        Auckland 0998, New Zealand
      </address>
      <span class="details__divider"></span>
      <div class="details__contact">
        P : +64 9 571 3048<br>
        F : +64 9 571 6285<br>
        sales@falconfreight.example.nz
      </div>
    </div>
  </section>
</main>
</body>
</html>
```